Newsletter template

I am looking for 2 newsletter templates. My website is in Wordpress and I want to use in mailchimp for lists.

One newsletter is for local clients of design remodeling firm to be sent monthly

Second newsletter is for web store offerings to be sent weekly.

Target Market(s)

Luxury home and leisure

Industry/Entity Type

Store

Requirements
Must have
• Use logos and colors to seamlessly integrate with website,

```html
<!DOCTYPE html>
<html lang="en">
<head>
<meta charset="utf-8">
<title>Newsletter – Product Offer</title>
<link href="https://fonts.googleapis.com/css2?family=Arimo:wght@400;700&family=PT+Sans:wght@700&display=swap" rel="stylesheet">
<style>
  :root {
    --bg: #ffffff;
    --charcoal: #434343;
    --cyan: #00a8c8;
    --cyan-light: #2bbad8;
    --lime: #d6e000;
    --body-text: #777777;
    --footer-text: #666666;
    --link: #1a9fc0;
    --rule: #e2e2e2;
    --grey-btn: #7a7a7a;
    --box-light: #f2f2f2;
    --box-mid: #d9d9d9;
    --social-blue: #4aa8d8;
    --social-navy: #3b5ea8;
    --social-amber: #e0a418;
  }
  * { margin: 0; padding: 0; box-sizing: border-box; }
  html, body {
    width: 1200px; height: 873px; overflow: hidden;
    background: var(--bg);
    font-family: "Arimo", Arial, sans-serif;
  }
  .newsletter { position: relative; width: 1200px; height: 873px; }

  .product-header {
    position: absolute; left: 92px; top: 21px; width: 1021px; height: 71px;
    display: flex; background: var(--charcoal);
  }
  .product-title {
    flex: 1; color: #fff; font-weight: 700; font-size: 26px;
    line-height: 71px; padding-left: 20px;
  }
  .product-price {
    width: 169px; background: var(--cyan); color: #fff; font-weight: 700;
    font-size: 26px; line-height: 71px; text-align: center;
  }

  .version-badge {
    position: absolute; left: 92px; top: 125px; width: 198px; height: 37px;
    background: var(--lime); color: #fff; font-weight: 700; font-size: 18px;
    line-height: 37px; text-align: center;
  }
  .product-visual {
    position: absolute; left: 180px; top: 205px; width: 320px; height: 270px;
    background: radial-gradient(ellipse at 50% 45%, var(--box-light) 0%, var(--box-mid) 45%, #ffffff 72%);
  }

  .product-details { position: absolute; left: 619px; top: 124px; width: 494px; }
  .product-description {
    color: var(--body-text); font-size: 19px; line-height: 32.5px;
  }
  .feature-list { list-style: none; margin-top: 20px; }
  .feature-item {
    display: flex; align-items: center; height: 66px;
    border-bottom: 1px dotted var(--rule);
    color: var(--link); font-size: 20px;
  }
  .feature-icon {
    width: 30px; height: 30px; border-radius: 50%; background: var(--charcoal);
    color: #bbb; font-size: 9px; line-height: 30px; text-align: center;
    margin-right: 10px; flex-shrink: 0;
  }

  .actions { position: absolute; top: 535px; left: 690px; display: flex; gap: 10px; }
  .action-btn {
    height: 36px; color: #fff; font-family: "PT Sans", Verdana, sans-serif;
    font-weight: 700; font-size: 16px; line-height: 36px; text-align: center;
    box-shadow: 0 3px 0 rgba(0,0,0,0.12);
  }
  .action-btn.view { width: 104px; background: var(--grey-btn); }
  .action-btn.order { width: 117px; background: var(--charcoal); }
  .action-btn.buy { width: 104px; background: var(--cyan-light); }

  .section-divider {
    position: absolute; left: 92px; top: 608px; width: 1021px; height: 14px;
  }

  .footer-contact {
    position: absolute; top: 666px; font-size: 19px; line-height: 32px;
    color: var(--footer-text);
  }
  .footer-contact.address { left: 92px; }
  .footer-contact.online { left: 444px; color: var(--link); }
  .social-links { position: absolute; left: 955px; top: 673px; display: flex; gap: 18px; }
  .social-dot { width: 39px; height: 39px; border-radius: 50%; }
  .social-dot.one { background: var(--social-blue); }
  .social-dot.two { background: var(--social-navy); }
  .social-dot.three { background: var(--social-amber); }

  .signature-rule { position: absolute; left: 92px; top: 760px; width: 318px; height: 8px; background: var(--charcoal); }
  .company-name {
    position: absolute; left: 92px; top: 798px; font-size: 24px; font-weight: 700;
    color: var(--charcoal);
  }
</style>
</head>
<body>
<div class="newsletter">
  <header class="product-header">
    <h1 class="product-title">Product name 3</h1>
    <div class="product-price">495$</div>
  </header>

  <div class="version-badge">UPDATED VERSION</div>
  <div class="product-visual" role="img" aria-label="Product box shot: white software box with a soft floral mark"></div>

  <section class="product-details">
    <p class="product-description">Donec porttitor quam vel purus venenatis rutrum. Nullam quam nibh, congue sed aliquet posuere, aliquam non lacus. Maecenas nec luctus neque. Aliquam sagittis tincidunt lectus, non semper lorem sollicitudin ac. Proin ac felis tortor, eu ultricies orci.</p>
    <ul class="feature-list">
      <li class="feature-item"><span class="feature-icon">ICO</span>Proin ac felis tortor, eu ultricies orci</li>
      <li class="feature-item"><span class="feature-icon">ICO</span>Aliquam sagittis tincidunt lectus</li>
      <li class="feature-item"><span class="feature-icon">ICO</span>Donec porttitor quam vel purus venenatis rutrum</li>
    </ul>
  </section>

  <nav class="actions">
    <div class="action-btn view">VIEW</div>
    <div class="action-btn order">ORDER</div>
    <div class="action-btn buy">BUY</div>
  </nav>

  <svg class="section-divider" viewBox="0 0 1021 14" preserveAspectRatio="none">
    <defs>
      <linearGradient id="fade" x1="0" x2="1">
        <stop offset="0" stop-color="#e6e6e6" stop-opacity="0"/>
        <stop offset="0.2" stop-color="#e6e6e6"/>
        <stop offset="0.8" stop-color="#e6e6e6"/>
        <stop offset="1" stop-color="#e6e6e6" stop-opacity="0"/>
      </linearGradient>
    </defs>
    <path d="M0 5 Q5 2 10 5 T20 5 T30 5" fill="none"/>
    <rect x="0" y="3" width="1021" height="3" fill="url(#fade)"/>
    <rect x="0" y="6" width="1021" height="8" fill="url(#fade)" opacity="0.35"/>
  </svg>

  <footer>
    <div class="footer-contact address">Company adress, City, State<br>Phone: 1-800-0000-000</div>
    <div class="footer-contact online">info@companywebsite.com<br>companywebsite.com</div>
    <div class="social-links">
      <span class="social-dot one"></span>
      <span class="social-dot two"></span>
      <span class="social-dot three"></span>
    </div>
    <div class="signature-rule"></div>
    <div class="company-name">Company name Ltd.</div>
  </footer>
</div>
</body>
</html>
```